Take my logo and make me some cool looking business cards

I've got a logo that we've trademarked so you can't change the logo but you can change it's color combo and find a fun way to incorporate it into a new business card design that is fresh, stylish, and can be applied to some cool medium cost materials (plastic, wood, metal, etc). Basically, we're looking for business cards that stand out in a good way.
Updates
Here's the logo we're currently using:
Thanks to everyone that has submitted designs. We've narrowed down to the top 4 designs and tried to eliminate old versions or designs that just didn't match our vision as quickly as we could. We don't plan on keeping this open for the full 9 days; we plan on selecting a design in the next 48 hours; with the goal of having something in the hands of a printer, preferably plastic printer, by Thursday AM Pacific Time.
Industry/Entity Type
Business
Requirements
Must have
- must include our existing logo

```html
<!DOCTYPE html>
<html lang="en">
<head>
<meta charset="utf-8">
<title>Tallow — Business Card</title>
<link href="https://fonts.googleapis.com/css2?family=Cinzel:wght@400;500&display=swap" rel="stylesheet">
<style>
  :root {
    --backdrop: #050505;
    --perforated-metal: #6f6969;
    --brushed-metal: #cbc3c3;
    --engraved-text: #f4f0f0;
    --card-edge: #8a8383;
  }
  html, body {
    margin: 0;
    width: 1200px;
    height: 1000px;
    overflow: hidden;
    background: var(--backdrop);
  }
  .business-card {
    position: absolute;
    left: 150px;
    top: 243px;
    width: 900px;
    height: 514px;
    border-radius: 30px;
    overflow: hidden;
    box-shadow: 0 0 0 2px var(--card-edge);
    font-family: "Cinzel", "Times New Roman", serif;
    color: var(--engraved-text);
  }
  .perforated-field {
    position: absolute;
    inset: 0;
    background: var(--perforated-metal);
  }
  .solid-panel {
    position: absolute;
    background: linear-gradient(100deg, #c4bcbc 0%, var(--brushed-metal) 45%, #d8d1d1 100%);
  }
  .identity-panel {
    left: 0;
    top: 38px;
    width: 340px;
    height: 72px;
    padding: 6px 0 0 26px;
    box-sizing: border-box;
  }
  .contact-panel {
    left: 410px;
    top: 38px;
    width: 490px;
    height: 205px;
    padding: 6px 0 0 22px;
    box-sizing: border-box;
  }
  .brand-panel {
    left: 230px;
    top: 340px;
    width: 670px;
    height: 150px;
    display: flex;
    align-items: center;
    padding-left: 22px;
    box-sizing: border-box;
  }
  .person-name, .person-role, .contact-line {
    margin: 0;
    font-weight: 400;
    letter-spacing: 0.02em;
    line-height: 1.15;
  }
  .person-name { font-size: 27px; }
  .person-role { font-size: 22px; }
  .contact-line { font-size: 28px; }
  .contact-line.street { margin-bottom: 2px; }
  .contact-line.phone { margin-top: 16px; font-size: 26px; }
  .contact-line.email { font-size: 25px; }
  .brand-name {
    margin: 0;
    font-size: 104px;
    font-weight: 400;
    letter-spacing: 0.01em;
    line-height: 1;
  }
</style>
</head>
<body>
  <article class="business-card">
    <div class="perforated-field" role="img" aria-label="Perforated metal surface with a fine honeycomb hole pattern"></div>

    <section class="solid-panel identity-panel">
      <p class="person-name">Morgan Hale</p>
      <p class="person-role">CEO</p>
    </section>

    <section class="solid-panel contact-panel">
      <p class="contact-line street">742 Alder Lane</p>
      <p class="contact-line">Cedar Point, CA 95021</p>
      <p class="contact-line phone">+1.555.014.2299</p>
      <p class="contact-line email">mh@tallowco.com</p>
    </section>

    <section class="solid-panel brand-panel">
      <p class="brand-name">TALLOW</p>
    </section>
  </article>
</body>
</html>
```